For lease banners for Businesses

I need to turn all of these banners into high quality graphics so I can get them printed on vinyl vertical banners that are 44"W x 88"H. So I need them most likely to be vector artwork, and ready to upload to a custom vinyl print shop.

```html
<!DOCTYPE html>
<html lang="en">
<head>
<meta charset="utf-8">
<title>Halcyon Investments – Vertical Leasing Banners</title>
<link href="https://fonts.googleapis.com/css2?family=Oswald:wght@400;500;600;700&family=Montserrat:wght@400;500;600&family=Kalam:wght@400&display=swap" rel="stylesheet">
<style>
:root{
  --ink:#25251f;
  --ink-deep:#1c1c18;
  --gold:#b8924b;
  --gold-soft:#c9a466;
  --white:#ffffff;
  --paper:#f2f2f1;
  --rule:#5d5a4c;
  --text-dim:#d8d5cc;
}
*{box-sizing:border-box;margin:0;padding:0}
html,body{width:1200px;height:3035px;overflow:hidden;background:var(--white)}
body{position:relative;font-family:"Montserrat",sans-serif;color:var(--white)}
.banner{position:absolute;width:422px;height:844px;overflow:hidden;background:var(--ink)}
.b-location{left:127px;top:138px}
.b-for-lease{left:653px;top:138px}
.b-your-name{left:127px;top:1085px;background:linear-gradient(180deg,#f4f4f4,#e4e5e6)}
.b-something{left:653px;top:1085px}
.b-now-leasing{left:127px;top:2016px}
.b-next-location{left:653px;top:2016px;background:linear-gradient(180deg,#1f2a1a 0%,#2a2c20 35%,#23231d 100%)}

.icon{width:24px;height:24px;fill:none;stroke:var(--gold);stroke-width:1.3;stroke-linecap:round;stroke-linejoin:round;flex:none}
.photo{position:absolute}

/* brand lockup */
.brand{display:flex;align-items:center;gap:12px;font-family:"Montserrat",sans-serif;font-weight:500;color:var(--white);line-height:1.1;white-space:nowrap}
.brand-square{flex:none;border:2px solid var(--gold)}
.brand-name{display:block;font-size:1em;letter-spacing:.2em}
.brand-sub{display:block;font-size:.46em;letter-spacing:.36em;margin-top:.2em}
.brand.stacked{flex-direction:column;gap:8px;text-align:center}

.rule-gold{position:absolute;height:2px;background:var(--gold)}
.oswald{font-family:"Oswald",sans-serif}

/* feature list */
.features{position:absolute;left:32px;right:32px;z-index:2}
.feature{display:flex;align-items:center;gap:18px;border-bottom:1px solid var(--rule)}
.feature:last-child{border-bottom:none}
.feature-title{font-family:"Oswald",sans-serif;font-weight:400;text-transform:uppercase;line-height:1.1}
.feature-desc{font-family:"Montserrat",sans-serif;color:var(--text-dim);line-height:1.2}

/* leasing band */
.lease-band{position:absolute;left:0;right:0;background:var(--gold);display:flex;align-items:center;justify-content:center;gap:14px;color:var(--ink)}
.lease-band .phone-dot{border-radius:50%;background:var(--ink);display:flex;align-items:center;justify-content:center}
.lease-band .phone-dot svg{fill:var(--gold);stroke:none}
.lease-band .label{font-family:"Oswald",sans-serif;font-weight:500;letter-spacing:.03em}
.lease-band .divider{width:1px;align-self:stretch;margin:8px 0;background:var(--ink)}
.lease-band .contact{font-family:"Oswald",sans-serif;line-height:1.05}
.lease-band .contact small{display:block;font-weight:400}
.lease-band .contact strong{display:block;font-weight:500}
.lease-band .contact em{display:block;font-style:normal;font-family:"Montserrat",sans-serif}

.tags{position:absolute;left:0;right:0;text-align:center;letter-spacing:.12em;white-space:nowrap}

/* ===== Banner 1 ===== */
.b-location .header{position:absolute;top:10px;left:0;right:0;display:flex;justify-content:center}
.b-location .header .brand-square{width:48px;height:48px}
.b-location .header .brand{font-size:17px;gap:10px}
.b-location .strip{position:absolute;left:0;right:0;display:flex;gap:3px;border-top:2px solid var(--gold);border-bottom:2px solid var(--gold)}
.b-location .strip .photo{position:relative;flex:1}
.b-location .headline{position:absolute;top:255px;left:0;right:0;text-align:center;font-family:"Oswald",sans-serif;font-weight:700;font-size:44px;line-height:1;letter-spacing:.02em}
.b-location .headline .gold{color:var(--gold)}
.b-location .headline p{font-weight:400;font-size:16px;margin-top:12px;letter-spacing:0}

/* ===== Banner 2 ===== */
.b-for-lease .header{position:absolute;top:32px;left:58px}
.b-for-lease .header .brand-square{width:74px;height:80px}
.b-for-lease .header .brand{font-size:34px;gap:24px}
.b-for-lease .title{position:absolute;top:140px;left:0;right:0;text-align:center;font-family:"Oswald",sans-serif;font-weight:700;font-size:132px;line-height:.9;z-index:2}
.b-for-lease .perks{position:absolute;top:612px;left:0;right:0;height:76px;display:flex;border-top:2px solid var(--gold)}
.b-for-lease .perk{flex:1;display:flex;flex-direction:column;align-items:center;justify-content:center;gap:8px;font-family:"Oswald",sans-serif;font-size:10px;letter-spacing:.08em;border-right:1px solid var(--gold)}
.b-for-lease .perk:last-child{border-right:none}
.b-for-lease .perk .icon{width:34px;height:34px}
.b-for-lease .phone-big{position:absolute;top:696px;left:0;right:0;text-align:center;font-family:"Oswald",sans-serif;font-weight:600;font-size:64px;line-height:1.15;white-space:nowrap}
.b-for-lease .diamond{position:absolute;top:783px;left:207px;width:8px;height:8px;background:var(--gold);transform:rotate(45deg)}
.b-for-lease .email{position:absolute;top:796px;left:0;right:0;text-align:center;font-size:22px;font-weight:500;white-space:nowrap}

/* ===== Banner 3 ===== */
.b-your-name .title{position:absolute;top:26px;left:36px;font-family:"Oswald",sans-serif;font-weight:700;font-size:96px;line-height:.82;color:var(--ink)}
.b-your-name .title span{color:var(--gold)}
.b-your-name .uses{position:absolute;top:302px;left:42px;list-style:none;z-index:2}
.b-your-name .uses li{display:flex;align-items:center;gap:28px;height:39px;font-weight:600;font-size:20px;color:var(--ink);letter-spacing:.02em}
.b-your-name .uses .icon{width:30px;height:30px}
.panel{position:absolute;left:0;right:0;bottom:0;background:var(--ink)}
.panel .brand-row{position:absolute;left:0;right:0;display:flex;justify-content:center}
.panel .brand-square{width:74px;height:80px}
.panel .brand{font-size:36px;gap:24px}
.contact-row{position:absolute;left:0;right:0;display:flex;align-items:center;justify-content:center;gap:12px}
.contact-row .lead{font-family:"Oswald",sans-serif;font-weight:500;font-size:28px;color:var(--gold)}
.contact-row .bar{width:1px;height:26px;background:var(--gold)}
.contact-row .lines{font-family:"Oswald",sans-serif;font-size:11px;line-height:1.45}
.contact-row .lines b{display:inline-block;width:7px;height:7px;border-radius:50%;background:var(--gold);margin-right:6px}

/* ===== Banner 4 ===== */
.b-something .header{position:absolute;top:16px;left:0;right:0;display:flex;justify-content:center}
.b-something .header .brand-square{width:50px;height:54px}
.b-something .header .brand{font-size:20px;gap:10px}
.b-something .headline{position:absolute;top:128px;left:33px;font-family:"Oswald",sans-serif;font-weight:700;font-size:53px;line-height:1.02;letter-spacing:.03em;z-index:2}
.b-something .headline .gold{color:var(--gold);font-size:78px;line-height:.95}
.b-something .headline .dot{color:var(--gold)}
.b-something .tags-left{position:absolute;top:385px;left:33px;font-family:"Montserrat",sans-serif;font-weight:600;font-size:13px;letter-spacing:.06em;z-index:2}
.b-something .tags-left span{color:var(--gold)}
.b-something .intro{position:absolute;top:422px;left:33px;font-family:"Oswald",sans-serif;font-size:18px;line-height:1.3;z-index:2}

/* ===== Banner 5 ===== */
.b-now-leasing .hero{position:absolute;top:0;left:0;right:0;height:377px;background:linear-gradient(90deg,#f3f1ec 0%,#ece8e0 42%,#b7a48f 60%,#8b5a44 78%,#6f7a52 100%)}
.b-now-leasing .hero-brand{position:absolute;top:58px;left:25px}
.b-now-leasing .hero-brand .brand-square{width:26px;height:26px}
.b-now-leasing .hero-brand .brand{font-size:13px;color:var(--ink);gap:8px}
.b-now-leasing .hero-title{position:absolute;top:100px;left:22px;font-family:"Oswald",sans-serif;font-weight:700;font-size:72px;line-height:.95;color:var(--ink)}
.b-now-leasing .hero-copy{position:absolute;top:258px;left:24px;font-family:"Oswald",sans-serif;font-size:15px;line-height:1.25;color:var(--ink)}
.b-now-leasing .hero-copy .gold{color:var(--gold);margin-top:8px;display:block}
.b-now-leasing .hero-copy .tagbox{display:inline-block;margin-top:8px;background:var(--ink);color:var(--white);font-size:13px;padding:3px 8px}
.b-now-leasing .perks{position:absolute;top:377px;left:0;right:0;height:124px;display:flex;padding:12px 6px}
.b-now-leasing .perk{flex:1;text-align:center;border-right:1px solid var(--gold);padding:0 4px}
.b-now-leasing .perk:last-child{border-right:none}
.b-now-leasing .perk .icon{width:28px;height:28px}
.b-now-leasing .perk h4{font-family:"Oswald",sans-serif;font-weight:400;font-size:11px;line-height:1.2;margin-top:6px}
.b-now-leasing .perk p{font-size:6px;line-height:1.3;color:var(--text-dim);margin-top:4px}
.b-now-leasing .gallery{position:absolute;top:501px;left:0;right:0;height:112px;display:flex;gap:3px}
.b-now-leasing .gallery .photo{position:relative;flex:1}
.b-now-leasing .ribbon{position:absolute;top:600px;left:70px;right:48px;height:24px;background:var(--gold);color:var(--ink);font-family:"Oswald",sans-serif;font-size:13px;display:flex;align-items:center;justify-content:center;transform:skewX(-8deg)}
.b-now-leasing .info-title{position:absolute;top:726px;left:0;right:0;text-align:center;font-family:"Oswald",sans-serif;font-weight:500;font-size:17px;color:var(--gold);letter-spacing:.06em}
.b-now-leasing .info-line{position:absolute;top:754px;left:0;right:0;display:flex;justify-content:center;gap:14px;font-family:"Oswald",sans-serif;font-size:17px;white-space:nowrap}
.b-now-leasing .info-line b{display:inline-block;width:10px;height:10px;border-radius:50%;background:var(--gold);margin-right:6px}
.b-now-leasing .footer-bar{position:absolute;bottom:0;left:0;right:0;height:38px;background:var(--gold);display:flex;align-items:center;color:var(--ink)}
.b-now-leasing .footer-item{flex:1;display:flex;align-items:center;justify-content:center;gap:5px;font-family:"Oswald",sans-serif;font-size:8.5px;line-height:1.15;border-right:1px solid var(--ink)}
.b-now-leasing .footer-item:last-child{border-right:none}
.b-now-leasing .footer-item .icon{stroke:var(--ink);width:18px;height:18px}

/* ===== Banner 6 ===== */
.b-next-location .headline{position:absolute;top:36px;left:0;right:0;text-align:center;font-family:"Oswald",sans-serif;font-weight:700;line-height:1;white-space:nowrap}
.b-next-location .headline .small{font-size:46px;font-weight:600}
.b-next-location .headline .big{font-size:84px;line-height:1.02}
.b-next-location .headline .gold{color:var(--gold)}
.b-next-location .script{position:absolute;top:296px;left:0;right:0;text-align:center;font-family:"Kalam",cursive;font-size:35px;line-height:1.05}
.b-next-location .perks{position:absolute;top:560px;left:0;right:0;height:92px;display:flex;background:var(--ink)}
.b-next-location .perk{flex:1;display:flex;flex-direction:column;align-items:center;justify-content:center;gap:8px;font-family:"Oswald",sans-serif;font-size:10px;line-height:1.2;text-align:center}
.b-next-location .perk .icon{width:30px;height:30px}
</style>
</head>
<body>

<svg width="0" height="0" style="position:absolute" aria-hidden="true">
  <defs>
    <symbol id="i-pin" viewBox="0 0 24 24"><path d="M12 22s7-7 7-12a7 7 0 0 0-14 0c0 5 7 12 7 12z"/><circle cx="12" cy="10" r="2.5"/></symbol>
    <symbol id="i-people" viewBox="0 0 24 24"><circle cx="7" cy="8" r="2.6"/><circle cx="17" cy="8" r="2.6"/><circle cx="12" cy="10.5" r="3"/><path d="M2 19c0-3 2-5 5-5M22 19c0-3-2-5-5-5M6 21c0-3.5 2.6-6 6-6s6 2.5 6 6"/></symbol>
    <symbol id="i-plan" viewBox="0 0 24 24"><rect x="3" y="3" width="18" height="18"/><path d="M3 12h8M11 3v6M11 15v6M15 12h6M15 12v4"/></symbol>
    <symbol id="i-hands" viewBox="0 0 24 24"><path d="M1 10l4-4 4 2 3-1.5 3 1 4-1 4 4M5 13l4 4 2-1 2 2 2-1 2 1 3-4M9 9l3 3 2-1"/></symbol>
    <symbol id="i-tools" viewBox="0 0 24 24"><path d="M5 3l5 5M3 5l5 5M7 7l13 13M19 3l-3 3 2 2 3-3M16 7L4 19l1.5 1.5L17.5 9"/></symbol>
    <symbol id="i-building" viewBox="0 0 24 24"><rect x="4" y="5" width="9" height="16"/><rect x="13" y="10" width="7" height="11"/><path d="M7 8h1M10 8h1M7 11h1M10 11h1M7 14h1M10 14h1M16 13h1M16 16h1M8 21v-3h1v3M2 21h20"/></symbol>
    <symbol id="i-phone" viewBox="0 0 24 24"><path d="M6.6 10.8a15 15 0 0 0 6.6 6.6l2.2-2.2a1 1 0 0 1 1-.25 11.4 11.4 0 0 0 3.6.57 1 1 0 0 1 1 1V20a1 1 0 0 1-1 1A17 17 0 0 1 3 4a1 1 0 0 1 1-1h3.5a1 1 0 0 1 1 1c0 1.25.2 2.45.57 3.57a1 1 0 0 1-.25 1z"/></symbol>
    <symbol id="i-bag" viewBox="0 0 24 24"><path d="M5 8h14l-1 13H6zM9 8V6a3 3 0 0 1 6 0v2"/></symbol>
    <symbol id="i-basket" viewBox="0 0 24 24"><path d="M3 10h18l-2 10H5zM7 10l4-6M17 10l-4-6M9 13v5M12 13v5M15 13v5"/></symbol>
    <symbol id="i-cup" viewBox="0 0 24 24"><path d="M4 10h13v4a5 5 0 0 1-5 5H9a5 5 0 0 1-5-5zM17 11h2a2 2 0 0 1 0 4h-2M3 21h16M9 3c-1 1 1 2 0 4M13 3c-1 1 1 2 0 4"/></symbol>
    <symbol id="i-case" viewBox="0 0 24 24"><rect x="3" y="7" width="18" height="13"/><path d="M9 7V5h6v2M3 12h18M11 12v2h2v-2"/></symbol>
    <symbol id="i-chart" viewBox="0 0 24 24"><path d="M3 21h18M6 18v-3M10 18v-6M14 18v-8M18 18V7M5 12l5-4 4 2 5-6"/></symbol>
    <symbol id="i-car" viewBox="0 0 24 24"><path d="M3 17v-5l2-5h10l2 5v5zM3 17v2M17 17v2M6 14h1M13 14h1"/><circle cx="19" cy="6" r="3"/><path d="M19 5v2"/></symbol>
    <symbol id="i-sign" viewBox="0 0 24 24"><path d="M12 3v18M12 5h6l2 2-2 2h-6M12 11H6l-2 2 2 2h6M8 21h8"/></symbol>
  </defs>
</svg>

<!-- Banner: This could be your next location (photo grid) -->
<section class="banner b-location">
  <div class="header">
    <div class="brand stacked"><div class="brand-square"></div><div><span class="brand-name">HALCYON</span><span class="brand-sub">INVESTMENTS</span></div></div>
  </div>
  <div class="strip" style="top:115px;height:140px">
    <div class="photo" role="img" aria-label="Latte art in a cup on a café table" style="background:radial-gradient(circle at 45% 60%,#d9b48a 0%,#7b4a28 35%,#2b1b12 80%)"></div>
    <div class="photo" role="img" aria-label="Two women shopping on a downtown street" style="background:linear-gradient(160deg,#b9aa98 0%,#6f655a 50%,#3b342d 100%)"></div>
  </div>
  <div class="headline">
    <div>THIS COULD BE</div>
    <div class="gold">YOUR NEXT</div>
    <div>LOCATION<span class="gold">.</span></div>
    <p>Build your business where people gather.</p>
  </div>
  <div class="strip" style="top:418px;height:112px">
    <div class="photo" role="img" aria-label="Boutique clothing store interior" style="background:linear-gradient(180deg,#6e4b2e 0%,#3b2818 60%,#a07a50 100%)"></div>
    <div class="photo" role="img" aria-label="Friends dining on an evening patio" style="background:radial-gradient(circle at 50% 20%,#c98f4a 0%,#5a3a22 45%,#1e1711 100%)"></div>
  </div>
  <div class="tags oswald" style="top:538px;font-size:12px;color:var(--gold)">RETAIL &nbsp;•&nbsp; RESTAURANT &nbsp;•&nbsp; OFFICE</div>
  <div class="features" style="top:556px">
    <div class="feature" style="height:36px"><svg class="icon" style="width:26px;height:26px"><use href="#i-pin"/></svg><div><div class="feature-title" style="font-size:13px">High visibility</div><div class="feature-desc" style="font-size:7.5px">Prime location with strong street exposure</div></div></div>
    <div class="feature" style="height:36px"><svg class="icon" style="width:26px;height:26px"><use href="#i-people"/></svg><div><div class="feature-title" style="font-size:13px">Downtown traffic</div><div class="feature-desc" style="font-size:7.5px">Surrounded by thriving businesses, events and foot traffic</div></div></div>
    <div class="feature" style="height:36px"><svg class="icon" style="width:26px;height:26px"><use href="#i-plan"/></svg><div><div class="feature-title" style="font-size:13px">Flexible floorplans</div><div class="feature-desc" style="font-size:7.5px">Customizable layouts to fit your business needs.</div></div></div>
    <div class="feature" style="height:36px"><svg class="icon" style="width:26px;height:26px"><use href="#i-hands"/></svg><div><div class="feature-title" style="font-size:13px">Local ownership</div><div class="feature-desc" style="font-size:7.5px">Proudly owned and invested in downtown</div></div></div>
    <div class="feature" style="height:36px"><svg class="icon" style="width:26px;height:26px"><use href="#i-tools"/></svg><div><div class="feature-title" style="font-size:13px">Build-to-suit options</div><div class="feature-desc" style="font-size:7.5px">Oppurtunities to create the perfect space.</div></div></div>
  </div>
  <div class="lease-band" style="top:738px;height:52px">
    <div class="phone-dot" style="width:30px;height:30px"><svg width="16" height="16"><use href="#i-phone"/></svg></div>
    <div class="label" style="font-size:16px;margin-right:14px">NOW LEASING</div>
    <div class="divider"></div>
    <div class="contact"><small style="font-size:9px">CALL OR TEXT</small><strong style="font-size:17px">555-210-4830</strong><em style="font-size:7.5px">leasing@halcyoninvest.com</em></div>
  </div>
  <div style="position:absolute;top:790px;left:0;right:0;height:54px;display:flex;justify-content:center;align-items:center">
    <div class="brand" style="font-size:20px;gap:14px"><div class="brand-square" style="width:38px;height:40px"></div><div><span class="brand-name">HALCYON</span><span class="brand-sub">INVESTMENTS</span></div></div>
  </div>
</section>

<!-- Banner: For lease -->
<section class="banner b-for-lease">
  <div class="header">
    <div class="brand"><div class="brand-square"></div><div><span class="brand-name">HALCYON</span><span class="brand-sub">INVESTMENTS</span></div></div>
  </div>
  <div class="rule-gold" style="top:130px;left:33px;right:33px"></div>
  <div class="photo" role="img" aria-label="Modern glass-front commercial building lit at dusk" style="top:262px;left:0;right:0;height:350px;background:radial-gradient(ellipse at 55% 70%,#c7904c 0%,#6a4a2c 28%,#2c2a26 60%,#1c1c1a 100%)"></div>
  <div class="title">FOR<br>LEASE</div>
  <div class="perks">
    <div class="perk"><svg class="icon"><use href="#i-building"/></svg>COMMERCIAL SPACE</div>
    <div class="perk"><svg class="icon"><use href="#i-hands"/></svg>FLEXIBLE OPPURTUNITY</div>
    <div class="perk"><svg class="icon"><use href="#i-people"/></svg>LOCALLY OWNED</div>
  </div>
  <div class="rule-gold" style="top:688px;left:0;right:0"></div>
  <div class="phone-big">555-210-4830</div>
  <div class="diamond"></div>
  <div class="email">leasing@halcyoninvest.com</div>
  <div style="position:absolute;bottom:0;left:0;right:0;height:6px;background:var(--gold)"></div>
</section>

<!-- Banner: Your name here -->
<section class="banner b-your-name">
  <div class="title">YOUR<br>NAME<br>HERE<span>.</span></div>
  <div class="rule-gold" style="top:282px;left:40px;width:350px"></div>
  <div class="photo" role="img" aria-label="Line sketch of a storefront with café seating" style="top:390px;right:0;width:300px;height:240px;background:linear-gradient(135deg,rgba(255,255,255,0) 0%,#e2e3e4 40%,#cfd0d2 100%)"></div>
  <ul class="uses">
    <li><svg class="icon"><use href="#i-bag"/></svg>RETAIL</li>
    <li><svg class="icon"><use href="#i-tools"/></svg>RESTAURANT</li>
    <li><svg class="icon"><use href="#i-basket"/></svg>BOUTIQUE</li>
    <li><svg class="icon"><use href="#i-cup"/></svg>COFFEE</li>
    <li><svg class="icon"><use href="#i-case"/></svg>OFFICE</li>
  </ul>
  <div class="panel" style="height:214px">
    <div class="brand-row" style="top:20px"><div class="brand"><div class="brand-square"></div><div><span class="brand-name">HALCYON</span><span class="brand-sub">INVESTMENTS</span></div></div></div>
    <div class="rule-gold" style="top:114px;left:32px;right:32px"></div>
    <div class="contact-row" style="top:130px"><div class="lead">LEASING NOW</div><div class="bar"></div><div class="lines"><div><b></b>555-210-4830</div><div><b></b>leasing@halcyoninvest.com</div></div></div>
    <div class="tags" style="top:180px;font-size:15px;font-weight:500">RETAIL &nbsp;<span style="color:var(--gold)">•</span>&nbsp; RESTAURANT &nbsp;<span style="color:var(--gold)">•</span>&nbsp; OFFICE</div>
  </div>
</section>

<!-- Banner: Something great belongs here -->
<section class="banner b-something">
  <div class="photo" role="img" aria-label="Historic brick downtown street at night, black and white" style="top:160px;left:0;right:0;height:400px;background:linear-gradient(90deg,var(--ink) 0%,rgba(37,37,31,.6) 40%,#6c6c6a 75%,#8d8d8b 100%)"></div>
  <div class="header"><div class="brand stacked"><div class="brand-square"></div><div><span class="brand-name">HALCYON</span><span class="brand-sub">INVESTMENTS</span></div></div></div>
  <div class="headline">SOMETHING<br><span class="gold">GREAT</span><br>BELONGS<br>HERE<span class="dot">.</span></div>
  <div class="tags-left">RETAIL <span>•</span> RESTAURANT <span>•</span> OFFICE</div>
  <div class="intro">Be part of Downtown Millbrook's<br>fastest-growing destination.</div>
  <div class="features" style="top:476px">
    <div class="feature" style="height:45px"><svg class="icon" style="width:30px;height:30px"><use href="#i-pin"/></svg><div><div class="feature-title" style="font-size:15px">High visibility</div><div class="feature-desc" style="font-size:8.5px">Prime location with strong street exposure</div></div></div>
    <div class="feature" style="height:45px"><svg class="icon" style="width:30px;height:30px"><use href="#i-people"/></svg><div><div class="feature-title" style="font-size:15px">Downtown traffic</div><div class="feature-desc" style="font-size:8.5px">Surrounded by thriving businesses, events and foot traffic</div></div></div>
    <div class="feature" style="height:42px"><svg class="icon" style="width:30px;height:30px"><use href="#i-plan"/></svg><div><div class="feature-title" style="font-size:15px">Flexible floorplans</div><div class="feature-desc" style="font-size:8.5px">Customizable layouts to fit your business needs.</div></div></div>
    <div class="feature" style="height:42px"><svg class="icon" style="width:30px;height:30px"><use href="#i-hands"/></svg><div><div class="feature-title" style="font-size:15px">Local ownership</div><div class="feature-desc" style="font-size:8.5px">Proudly owned and invested in downtown</div></div></div>
    <div class="feature" style="height:44px"><svg class="icon" style="width:30px;height:30px"><use href="#i-tools"/></svg><div><div class="feature-title" style="font-size:15px">Build-to-suit options</div><div class="feature-desc" style="font-size:8.5px">Oppurtunities to create the perfect space.</div></div></div>
  </div>
  <div class="lease-band" style="top:720px;height:60px">
    <div class="phone-dot" style="width:32px;height:32px"><svg width="17" height="17"><use href="#i-phone"/></svg></div>
    <div class="label" style="font-size:19px;margin-right:14px">NOW LEASING</div>
    <div class="divider"></div>
    <div class="contact"><small style="font-size:11px">CALL OR TEXT</small><strong style="font-size:21px">555-210-4830</strong><em style="font-size:9px">leasing@halcyoninvest.com</em></div>
  </div>
  <div style="position:absolute;top:780px;left:0;right:0;height:64px;display:flex;justify-content:center;align-items:center">
    <div class="brand" style="font-size:22px;gap:16px"><div class="brand-square" style="width:40px;height:44px"></div><div><span class="brand-name">HALCYON</span><span class="brand-sub">INVESTMENTS</span></div></div>
  </div>
</section>

<!-- Banner: Now leasing (downtown) -->
<section class="banner b-now-leasing">
  <div class="hero" role="img" aria-label="Brick storefront building on a tree-lined downtown street"></div>
  <div class="hero-brand"><div class="brand"><div class="brand-square"></div><div><span class="brand-name">HALCYON</span><span class="brand-sub">INVESTMENTS</span></div></div></div>
  <div class="hero-title">NOW<br>LEASING</div>
  <div class="rule-gold" style="top:248px;left:24px;width:218px"></div>
  <div class="hero-copy">PREMIER RETAIL, RESTAURANT<br>&amp; OFFICE SPACE<span class="gold">IN THE HEART OF DOWNTOWN MILLBROOK</span><span class="tagbox">BE PART OF SOMETHING EXCEPTIONAL.</span></div>
  <div class="perks">
    <div class="perk"><svg class="icon"><use href="#i-pin"/></svg><h4>HIGH<br>VISIBILITY</h4><p>Prime location with strong street exposure</p></div>
    <div class="perk"><svg class="icon"><use href="#i-people"/></svg><h4>GROWING<br>COMMUNITY</h4><p>Surrounded by thriving businesses, events and foot traffic</p></div>
    <div class="perk"><svg class="icon"><use href="#i-building"/></svg><h4>FLEXIBLE<br>SPACES</h4><p>Customizable layouts to fit your business needs</p></div>
    <div class="perk"><svg class="icon"><use href="#i-car"/></svg><h4>GREAT<br>ACCESS</h4><p>Easy access &amp; convenient parking nearby</p></div>
    <div class="perk"><svg class="icon"><use href="#i-chart"/></svg><h4>BUILT FOR<br>SUCCESS</h4><p>A downtown environment where business thrives</p></div>
  </div>
  <div class="gallery">
    <div class="photo" role="img" aria-label="Restaurant patio with string lights" style="background:linear-gradient(180deg,#6a4a2e,#2e2218)"></div>
    <div class="photo" role="img" aria-label="Street clock surrounded by flowers" style="background:linear-gradient(180deg,#7d8a6a,#4a5236)"></div>
    <div class="photo" role="img" aria-label="Evening crowd at a downtown square" style="background:linear-gradient(180deg,#34425a,#6b5236)"></div>
    <div class="photo" role="img" aria-label="Brick storefronts along a sidewalk" style="background:linear-gradient(180deg,#a7aab0,#6e5142)"></div>
  </div>
  <div class="ribbon">YOUR BUSINESS, YOUR SPACE, YOUR FUTURE.</div>
  <div style="position:absolute;top:634px;left:0;right:0;display:flex;justify-content:center">
    <div class="brand" style="font-size:36px;gap:24px"><div class="brand-square" style="width:74px;height:80px"></div><div><span class="brand-name">HALCYON</span><span class="brand-sub">INVESTMENTS</span></div></div>
  </div>
  <div class="rule-gold" style="top:722px;left:32px;right:32px;height:1px"></div>
  <div class="info-title">LEASING INFORMATION</div>
  <div class="info-line"><span><b></b>555-210-4830</span><span><b></b>leasing@halcyoninvest.com</span></div>
  <div class="footer-bar">
    <div class="footer-item"><svg class="icon"><use href="#i-pin"/></svg>DOWNTOWN MILLBROOK</div>
    <div class="footer-item"><svg class="icon"><use href="#i-sign"/></svg><span>JOIN A VIBRANT<br>DOWNTOWN DESTINATION</span></div>
    <div class="footer-item"><svg class="icon"><use href="#i-people"/></svg><span>BE SEEN. BE SUCCESSFUL.<br>BELONG DOWNTOWN.</span></div>
  </div>
</section>

<!-- Banner: This could be your next location (feature) -->
<section class="banner b-next-location">
  <div class="photo" role="img" aria-label="Blurred green foliage background" style="inset:0;background:radial-gradient(ellipse at 20% 15%,rgba(90,110,60,.45),transparent 55%),radial-gradient(ellipse at 85% 30%,rgba(120,100,50,.35),transparent 50%)"></div>
  <div class="headline">
    <div class="small">THIS COULD BE</div>
    <div class="big">YOUR NEXT</div>
    <div class="big gold">LOCATION.</div>
  </div>
  <div class="rule-gold" style="top:278px;left:46px;right:34px"></div>
  <div class="script">Build your business<br>where people gather.</div>
  <div class="photo" role="img" aria-label="Friends sharing a meal at an outdoor café" style="top:385px;left:0;right:0;height:175px;background:linear-gradient(180deg,rgba(40,40,30,0) 0%,#6b5a44 35%,#3a3025 100%)"></div>
  <div class="perks">
    <div class="perk"><svg class="icon"><use href="#i-pin"/></svg>HIGH<br>VISIBILITY</div>
    <div class="perk"><svg class="icon"><use href="#i-people"/></svg>GROWING<br>COMMUNITY</div>
    <div class="perk"><svg class="icon"><use href="#i-plan"/></svg>FLEXIBLE<br>FLOORPLANS</div>
    <div class="perk"><svg class="icon"><use href="#i-pin"/></svg>LOCAL<br>OWNERSHIP</div>
  </div>
  <div class="panel" style="height:192px">
    <div class="brand-row" style="top:8px"><div class="brand"><div class="brand-square"></div><div><span class="brand-name">HALCYON</span><span class="brand-sub">INVESTMENTS</span></div></div></div>
    <div class="rule-gold" style="top:98px;left:22px;right:22px"></div>
    <div class="contact-row" style="top:110px"><div class="lead">LEASING NOW</div><div class="bar"></div><div class="lines"><div><b></b>555-210-4830</div><div><b></b>leasing@halcyoninvest.com</div></div></div>
    <div class="tags" style="top:158px;font-size:15px;font-weight:500">RETAIL &nbsp;<span style="color:var(--gold)">•</span>&nbsp; RESTAURANT &nbsp;<span style="color:var(--gold)">•</span>&nbsp; OFFICE</div>
  </div>
</section>

</body>
</html>
```